Jewelry store needs fully functional Ecommerce website

Web Design Brief for our E-commerce Jewelry retail store.
Description

We need a fully coded Vendora website. The Vendora site will need to be fully functional with an Ecommerce integration (fully integrated with Coinlet and All other gateways) and will need to be SEO optimized.
We sell jewelry items like: rings, earrings, necklaces etc. The website should have an elegant, modern, professional, fun, look.

***We would like the website to look and function similarly to this website:
https://velvetrune.com

Color Preference
Colors to be used are white background with black font and light pink/ purple/ gold tints. We have attached our logo as reference.

Functionalities
The store will function like a typical Ecommerce jewelry store, using the products/categories as the starting page. Going into individual product pages by selecting images and leading to a detailed “buy now” page for the selected product.

Target Market
Jewelry lovers.

Should Not Have:
- - Dull and common design
- - Messy/unstructured navigation

Coded - Design and coding required
Target Audience are women from 16-50 years old.
We will need to be able to add products and make modifications to the website as needed.

We need the following apps installed and Operating:
-Shelf Tally; Parcel Finder (rename “track your order”) ; Query Desk (Questions and Answers) ; Vimt Reviews; Textazo; Brundel Email Marketing ; Tavolo (Chatterloop messenger bump) ; Brisk multi- currency (translate currency to buyer) ; Pricewise Extra ; Swift Reach form App
We will need all products imported: (below is information for importing products). We will provide all links that serve entire active item product catalog in vendoras import format:
DataFeed:

If you are getting started with Vendora, a combination of the Vendora Import Format and XML feeds is ideal. The Vendora Import Format will output a file that can be uploaded into Vendora’s product database. After you import, you can use the XML feed and a third party app to keep the inventory up to date in real time, take down items that go out of stock etc., all without regular human intervention. There a several Vendora apps that can do this type of feed integration. We have had a good experience with Shelf Tally, which is an app that can be configured to accept our XML feed and update products on a set schedule. You can even set your own margins based on our wholesale price with this app.

Vendora Formatted HTML TableTo make it easier to get started on Vendora, we included a format that outputs the required fields for a product import in Vendora. In order to use the embedded Excel file, first open the file (Auto-Vendora-Datasheet-Format.xslx), Refresh it (under Data tab), and then Save As with a new file name in a CSV (UTF-8) file. That file can then be split into smaller CSV files (if there is a limit on the number of products per file) for import into Vendora.

Target Market(s)

Jewelry Lovers

Industry/Entity Type

Jewelry Store

Coding

Number of Pages Required

5+ page

Colors
eda3c7
d3a5cc
ffffff

Requirements
Must have
• Color Preference
Colors to be used are white background with black font and light pink/ purple/ gold tints.

https://velvetrune.com
Should not have
• Should Not Have:

```html
<!DOCTYPE html>
<html lang="en">
<head>
<meta charset="utf-8">
<title>Lumen Adore — Fine Jewelry</title>
<link rel="stylesheet" href="https://fonts.googleapis.com/css2?family=Playfair+Display:ital,wght@0,400;0,500;1,400&family=Montserrat:wght@400;500;600&display=swap">
<style>
:root{
  --pink:#eda3c7;
  --pink-deep:#e48bbb;
  --lilac:#d3a5cc;
  --gold:#e6ad7e;
  --ink:#1a1a1a;
  --muted:#444;
  --band:#f5f5f7;
  --white:#ffffff;
  --serif:'Playfair Display', Georgia, serif;
  --sans:'Montserrat', Arial, sans-serif;
}
*{box-sizing:border-box;margin:0;padding:0}
html,body{width:1200px;height:4129px;overflow:hidden;background:var(--white)}
body{font-family:var(--sans);color:var(--ink)}
.page{position:relative;width:1200px;height:4129px;overflow:hidden}
.abs{position:absolute}
.band{position:absolute;left:0;width:1200px;background:var(--band)}
.photo{position:absolute}
.serif{font-family:var(--serif);font-weight:400;letter-spacing:.04em;text-transform:uppercase}
.btn{position:absolute;display:flex;align-items:center;justify-content:center;font-size:14px;font-weight:500;letter-spacing:.02em;text-transform:uppercase;color:var(--white);background:var(--pink)}
.btn--outline{background:var(--white);color:var(--pink-deep);border:2px solid var(--pink)}
.body-text{font-size:12.5px;line-height:20px;color:var(--muted)}

/* top bar & nav */
.topbar{position:absolute;top:0;left:0;width:1200px;height:29px;background:#111;color:#fff;font-size:10.5px}
.topbar .currency{position:absolute;left:149px;top:8px}
.topbar .help{position:absolute;right:151px;top:8px}
.nav{position:absolute;top:29px;left:0;width:1200px;height:61px;border-bottom:1px solid #e6e6e6}
.nav__links{position:absolute;left:149px;top:25px;display:flex;gap:30px;font-size:11px;font-weight:500}
.nav__brand{position:absolute;left:0;width:1200px;top:18px;text-align:center;font-family:var(--serif);font-size:20px;color:var(--ink)}
.nav__icons{position:absolute;right:148px;top:20px;display:flex;gap:30px}

/* hero */
.hero__title{position:absolute;left:149px;top:188px;font-family:var(--serif);font-size:47px;line-height:50px;letter-spacing:.02em}
.hero__title small{font-size:30px}
.hero__title em{font-size:30px;font-style:italic}
.dot{color:var(--pink-deep)}
.hero__text{position:absolute;left:150px;top:322px;width:330px}

/* about */
.eyebrow{position:absolute;font-size:12.5px;font-weight:500;color:var(--pink-deep);text-transform:uppercase}
.about__title{position:absolute;left:527px;top:742px;font-size:28px;line-height:41px;letter-spacing:.06em}
.about__text{position:absolute;left:527px;top:935px;width:290px}
.about__link{position:absolute;left:527px;top:1024px;font-family:var(--serif);font-size:17px;letter-spacing:.03em}

/* section titles */
.section-title{position:absolute;font-size:28px;letter-spacing:.06em}

/* product cards */
.product{position:absolute;top:1264px;width:285px}
.product__img{width:285px;height:359px}
.product__name{margin-top:12px;text-align:center;font-family:var(--serif);font-size:17px;letter-spacing:.08em;text-transform:uppercase}
.product__meta{margin-top:10px;display:flex;align-items:center;justify-content:center;gap:14px;font-size:11px;color:#555}
.stars{color:var(--gold);letter-spacing:3px;font-size:11px}
.price-old{text-decoration:line-through;font-size:12px}
.price{font-size:19px;font-weight:500;color:var(--ink)}
.arrow{position:absolute}

/* explore */
.explore-card{position:absolute;top:1946px;width:302px}
.explore-card__img{width:302px;height:353px}
.explore-card__label{margin-top:22px;font-size:13.5px;font-weight:600;letter-spacing:.15em;text-transform:uppercase}
.explore-card__desc{margin-top:12px;font-size:12px;color:var(--muted);white-space:nowrap}

/* testimonial */
.quote{position:absolute;left:498px;top:2925px;font-family:var(--serif);font-size:130px;line-height:120px;color:var(--pink)}
.testi__title{position:absolute;left:600px;width:450px;top:2968px;text-align:center;font-size:27px;line-height:41px;letter-spacing:.08em}
.testi__text{position:absolute;left:620px;width:410px;top:3070px;text-align:center;font-size:12.5px;line-height:20px;color:var(--muted)}
.testi__stars{position:absolute;left:600px;width:450px;top:3165px;text-align:center;color:var(--gold);font-size:16px;letter-spacing:6px}
.testi__name{position:absolute;left:600px;width:450px;top:3202px;text-align:center;font-size:13px;font-weight:600;letter-spacing:.1em}

/* vip */
.vip__title{position:absolute;left:0;width:1200px;top:3458px;text-align:center;font-size:27px;letter-spacing:.06em}
.vip__text{position:absolute;left:0;width:1200px;top:3528px;text-align:center;font-size:14px;color:var(--muted)}
.vip__input{position:absolute;left:383px;top:3592px;width:208px;height:36px;border:1.5px solid var(--pink);background:#fff;font-size:13px;font-style:italic;color:#aaa;padding:9px 20px}

/* features */
.feature{position:absolute;top:3764px;display:flex;gap:14px;align-items:center;font-size:11px;line-height:16px;color:var(--muted);letter-spacing:.03em}
.rule{position:absolute;left:148px;top:3837px;width:900px;height:1px;background:#f0c7dc}

/* footer */
.footer__brand{position:absolute;left:154px;top:3892px;font-family:var(--serif);font-size:22px}
.footer__social{position:absolute;left:149px;top:3962px;display:flex;gap:26px}
.footer__social span{width:18px;height:18px;border:1.8px solid var(--pink);border-radius:50%}
.footer__label{position:absolute;left:149px;top:4015px;font-size:11.5px;font-weight:600;letter-spacing:.04em}
.footer__pay{position:absolute;left:149px;top:4050px;display:flex;gap:24px;font-size:13px;font-weight:600;color:var(--ink)}
.footer-col{position:absolute;top:3882px;font-size:12px;letter-spacing:.06em;color:var(--muted)}
.footer-col h4{font-size:11.5px;font-weight:600;color:var(--ink);margin-bottom:15px;letter-spacing:.06em}
.footer-col li{list-style:none;height:27px}
</style>
</head>
<body>
<div class="page">

  <!-- top bar -->
  <div class="topbar">
    <span class="currency">USD($) &#8964;</span>
    <span class="help">Have questions ?</span>
  </div>

  <!-- navigation -->
  <header class="nav">
    <nav class="nav__links"><span>SHOP</span><span>ABOUT</span><span>SERVICE</span></nav>
    <div class="nav__brand">Lumen Adore</div>
    <div class="nav__icons">
      <svg width="20" height="20" viewBox="0 0 20 20" fill="none" stroke="#111" stroke-width="1.6"><circle cx="8.5" cy="8.5" r="6.5"/><path d="M13.5 13.5L19 19"/></svg>
      <svg width="20" height="20" viewBox="0 0 20 20" fill="none" stroke="#111" stroke-width="1.6"><circle cx="10" cy="6.5" r="4.5"/><path d="M3 19c0-4 3-6.5 7-6.5s7 2.5 7 6.5"/></svg>
      <svg width="20" height="20" viewBox="0 0 20 20" fill="none" stroke="#111" stroke-width="1.6"><path d="M10 18S2 12.5 2 7a4.2 4.2 0 018-1.8A4.2 4.2 0 0118 7c0 5.5-8 11-8 11z"/></svg>
      <svg width="20" height="20" viewBox="0 0 20 20" fill="none" stroke="#111" stroke-width="1.6"><path d="M4 6h12l-1 13H5z"/><path d="M7 8V4.5a3 3 0 016 0V8"/></svg>
    </div>
  </header>

  <!-- hero -->
  <section class="hero">
    <div class="photo" role="img" aria-label="Woman with auburn hair touching her cheek, wearing a diamond ring and earring" style="left:640px;top:90px;width:560px;height:487px;background:linear-gradient(110deg,#ffffff 0%,#f3e6df 18%,#c98f6f 45%,#8a4a2e 75%,#c07a5a 100%)"></div>
    <h1 class="hero__title"><span>ELEGANCE</span> <small>FOR EVERY</small><br><em>SPECIAL</em> MOMENT<span class="dot">.</span></h1>
    <p class="hero__text body-text">There is no better gift than one that holds special meaning. Speak volumes this season with symbolic designs they'll treasure for life.</p>
    <a class="btn" style="left:149px;top:425px;width:170px;height:43px">Visit Shop</a>
  </section>

  <!-- about -->
  <div class="band" style="top:577px;height:341px"></div>
  <section class="about">
    <div class="photo" role="img" aria-label="Hands with white manicure holding a rose gold diamond ring" style="left:149px;top:666px;width:332px;height:443px;background:linear-gradient(160deg,#e7c3cd 0%,#f2e3e6 35%,#e9d2cf 60%,#d9b6ad 100%)"></div>
    <div class="eyebrow" style="left:527px;top:698px">Meet Lumen Adore</div>
    <h2 class="about__title serif">Built to withstand,<br>change, and move<br>through life<br>with you<span class="dot">.</span></h2>
    <div class="photo" role="img" aria-label="Smiling woman covering her mouth with a ringed hand" style="left:863px;top:751px;width:185px;height:225px;background:linear-gradient(135deg,#5e4a3f 0%,#c9a593 45%,#ecdcd4 100%)"></div>
    <p class="about__text body-text">We create design-forward, customizable fine jewelry that empowers modern woman to buy for themselves, on their own terms.</p>
    <a class="about__link">Learn More</a>
  </section>

  <!-- most popular -->
  <h2 class="section-title serif" style="left:0;width:1200px;text-align:center;top:1190px">Most Popular</h2>
  <svg class="arrow" style="left:84px;top:1433px" width="14" height="22" viewBox="0 0 14 22" fill="none" stroke="#222" stroke-width="1.6"><path d="M11 2L3 11l8 9"/></svg>
  <svg class="arrow" style="left:1100px;top:1433px" width="14" height="22" viewBox="0 0 14 22" fill="none" stroke="#222" stroke-width="1.6"><path d="M3 2l8 9-8 9"/></svg>

  <article class="product" style="left:149px">
    <div class="product__img" role="img" aria-label="Hand wearing a diamond ring beside a matching earring" style="background:linear-gradient(150deg,#e9c7c0 0%,#f3ddd6 50%,#dfb7b0 100%)"></div>
    <h3 class="product__name">Pearl Earring &amp; Ring</h3>
    <div class="product__meta"><span class="stars">★★★★★</span><span>(145)</span><span class="price-old">$100</span><span class="price">$90</span></div>
  </article>
  <article class="product" style="left:457px">
    <div class="product__img" role="img" aria-label="Woman in a pink top wearing a pendant necklace" style="background:linear-gradient(160deg,#d9b8a3 0%,#efd7cf 45%,#f6cfe0 100%)"></div>
    <h3 class="product__name">Pearl Necklace</h3>
    <div class="product__meta"><span class="stars">★★★★★</span><span>(112)</span><span class="price-old">$100</span><span class="price">$120</span></div>
  </article>
  <article class="product" style="left:764px">
    <div class="product__img" role="img" aria-label="Wrist wearing a fine rose gold bracelet" style="background:linear-gradient(150deg,#f0d9d2 0%,#e6c3b8 55%,#d8aea3 100%)"></div>
    <h3 class="product__name">Pearl Bracelet</h3>
    <div class="product__meta"><span class="stars">★★★★★</span><span>(99)</span><span class="price-old">$100</span><span class="price">$75</span></div>
  </article>

  <a class="btn" style="left:149px;top:1745px;width:170px;height:43px">Shop Now</a>
  <a class="btn btn--outline" style="left:881px;top:1745px;width:168px;height:43px">Discover</a>

  <!-- explore -->
  <div class="band" style="top:2080px;height:788px"></div>
  <h2 class="section-title serif" style="left:148px;top:1870px">Explore</h2>
  <svg class="arrow" style="left:1047px;top:1880px" width="12" height="20" viewBox="0 0 12 20" fill="none" stroke="#999" stroke-width="1.6"><path d="M10 2L3 10l7 8"/></svg>
  <svg class="arrow" style="left:1083px;top:1880px" width="12" height="20" viewBox="0 0 12 20" fill="none" stroke="#222" stroke-width="1.6"><path d="M2 2l7 8-7 8"/></svg>

  <article class="explore-card" style="left:151px">
    <div class="explore-card__img" role="img" aria-label="Hands wearing a flower-shaped ring" style="background:linear-gradient(150deg,#f1e4e3 0%,#e8cfca 50%,#f4ebea 100%)"></div>
    <h3 class="explore-card__label">Alluring Rings</h3>
    <p class="explore-card__desc">Eye-catching rings that will capture attention.</p>
  </article>
  <article class="explore-card" style="left:473px">
    <div class="explore-card__img" role="img" aria-label="Red gift boxes and triangle earrings on a pink surface" style="background:linear-gradient(140deg,#f8d7d5 0%,#f3b5ad 45%,#e0473f 75%,#f6c2bd 100%)"></div>
    <h3 class="explore-card__label">Precious Gifts</h3>
    <p class="explore-card__desc">Eye-catching rings that will capture attention.</p>
  </article>
  <article class="explore-card" style="left:795px">
    <div class="explore-card__img" role="img" aria-label="Wrist with a silver charm bracelet over pink knitwear" style="background:linear-gradient(150deg,#c48f9b 0%,#d9aab3 50%,#b97e8b 100%)"></div>
    <h3 class="explore-card__label">Imposing Bracelets</h3>
    <p class="explore-card__desc">Eye-catching rings that will capture attention.</p>
  </article>
  <article class="explore-card" style="left:1117px">
    <div class="explore-card__img" role="img" aria-label="Woman wearing a necklace" style="background:linear-gradient(150deg,#e6b9a6 0%,#f1c9d6 100%)"></div>
    <h3 class="explore-card__label">Necklaces</h3>
    <p class="explore-card__desc">Eye-catching rings that will capture attention.</p>
  </article>

  <!-- why -->
  <h2 class="section-title serif" style="left:149px;top:2505px">Why Lumen Adore</h2>
  <p class="body-text abs" style="left:149px;top:2573px;width:290px">On a mission to reinvent an outdated jewelry industry, Lumen Adore is hitting social media by storm, crafting irresistible gemstone jewelry we can only describe as magic.</p>
  <a class="btn" style="left:149px;top:2696px;width:169px;height:44px">Shop Now</a>
  <div class="photo" role="img" aria-label="Woman in a pink top fastening a pendant necklace" style="left:570px;top:2459px;width:479px;height:338px;background:linear-gradient(180deg,#f6c9d3 0%,#efc3c0 45%,#f7d3e3 100%)"></div>

  <!-- testimonial -->
  <div class="photo" role="img" aria-label="Smiling woman with curly hair in a striped top" style="left:152px;top:2932px;width:396px;height:352px;background:linear-gradient(180deg,#fbd3ea 0%,#f6c6df 40%,#c98a6e 70%,#e8c0c4 100%)"></div>
  <div class="quote">&#8220;</div>
  <h2 class="testi__title serif">What our customers<br>are saying</h2>
  <p class="testi__text">I was quite surprised to see the quality of this jewellery. I got it at a huge discount. The way it is packed, it would make a good gift. I love the pearls and the golden leaf.</p>
  <div class="testi__stars">★★★★★</div>
  <div class="testi__name">CLARA WHITBY</div>
  <svg class="arrow" style="left:805px;top:3257px" width="10" height="16" viewBox="0 0 10 16" fill="none" stroke="#999" stroke-width="1.5"><path d="M8 1L2 8l6 7"/></svg>
  <svg class="arrow" style="left:834px;top:3257px" width="10" height="16" viewBox="0 0 10 16" fill="none" stroke="#222" stroke-width="1.5"><path d="M2 1l6 7-6 7"/></svg>

  <!-- vip -->
  <div class="band" style="top:3372px;height:345px"></div>
  <h2 class="vip__title serif">Become a Lumen Adore VIP and save 10%</h2>
  <p class="vip__text">Dress up your inbox with Lumen Adore updates and be the first to know about sales, new collections, and more!</p>
  <div class="vip__input">Enter your email</div>
  <a class="btn" style="left:607px;top:3592px;width:210px;height:36px">Subscribe Now</a>

  <!-- features -->
  <div class="feature" style="left:150px">
    <svg width="38" height="28" viewBox="0 0 38 28" fill="none" stroke="#222" stroke-width="1.5"><path d="M2 5h22v15H2zM24 10h7l5 6v4H24"/><circle cx="9" cy="22" r="3"/><circle cx="29" cy="22" r="3"/></svg>
    <span>Free delivery for<br>orders over 100$</span>
  </div>
  <div class="feature" style="left:355px">
    <svg width="30" height="30" viewBox="0 0 30 30" fill="none" stroke="#222" stroke-width="1.5"><path d="M25 15a10 10 0 11-3-7.1"/><path d="M22 3v5h-5"/><path d="M10 15l3.5 3.5L20 12"/></svg>
    <span>Hassle-free returns:<br>easy exchange or return items</span>
  </div>
  <div class="feature" style="left:632px">
    <svg width="28" height="28" viewBox="0 0 28 28" fill="none" stroke="#222" stroke-width="1.5"><path d="M14 2l3.6 7.6 8.2 1-6 5.7 1.5 8.2L14 20.5l-7.3 4 1.5-8.2-6-5.7 8.2-1z"/></svg>
    <span>Over 1 million followers<br>&amp; 10,000 reviews</span>
  </div>
  <div class="feature" style="left:866px">
    <svg width="28" height="26" viewBox="0 0 28 26" fill="none" stroke="#222" stroke-width="1.5"><rect x="2" y="3" width="20" height="14"/><path d="M2 7h20"/><rect x="14" y="13" width="12" height="10"/></svg>
    <span>Secure payment<br>Cardova, Medalcard, Coinlet</span>
  </div>
  <div class="rule"></div>

  <!-- footer -->
  <footer>
    <div class="footer__brand">Lumen Adore</div>
    <div class="footer__social" aria-label="Social links"><span></span><span></span><span></span></div>
    <div class="footer__label">SECURE PAYMENT</div>
    <div class="footer__pay"><span>Coinlet</span><span>Medalcard</span><span>Cardova</span></div>

    <div class="footer-col" style="left:428px">
      <h4>LUMEN ADORE</h4>
      <ul><li>STORY</li><li>NEWS &amp; PRESS</li><li>VIDEOS</li><li>INSPIRE</li><li>STOCKISTS</li><li>THE EDIT</li></ul>
    </div>
    <div class="footer-col" style="left:663px">
      <h4>CONTACT</h4>
      <ul><li>01632 960418</li><li>GENERAL ENQUIRIES</li><li>ORDER ENQUIRIES</li><li>PRESS FEATURES</li><li>OUR STORES</li><li>VACANCIES</li></ul>
    </div>
    <div class="footer-col" style="left:939px">
      <h4>HELP WITH...</h4>
      <ul><li>DELIVERY</li><li>RETURNS</li><li>LOYALTY</li><li>FAQS</li><li>SIZE GUIDES</li><li>T'S &amp; C'S</li><li>PRIVACY POLICY</li></ul>
    </div>
  </footer>

</div>
</body>
</html>
```